Business Cards for an 'affordable luxury' inner city home builder in Calgary.

We need a business card design that emulates the progressive, innovative, culture of our company and the modern style of our homes. Use our website www.velmarbuilds-ex.com as a reference for the product we build.

Our company builds homes in the inner city space of Calgary, Alberta. We build affordable luxury.

Target Market(s)

Young professional Families

Contact Information for Business Card

Try to maintain consistency with the logo font and the card font.

Requirements
Must have
• The details must include: Name, education, title, phone number, website and email (Address is not as important)
• The design must be uniques (like our logo), elegant, sophisticated and modern.

```html
<!DOCTYPE html>
<html lang="en">
<head>
<meta charset="utf-8">
<title>Velmar Builds Ltd – Business Card</title>
<link rel="stylesheet" href="https://fonts.googleapis.com/css2?family=Source+Sans+3:wght@300;400;600;700&display=swap">
<style>
  :root {
    --backdrop: #596067;
    --card: #ffffff;
    --ink: #111111;
    --ink-soft: #7d7d7d;
    --band: #333333;
    --band-text: #f2f2f2;
    --deco-dark: #222222;
    --deco-mid: #858585;
    --deco-light: #c3c3c3;
  }
  * { box-sizing: border-box; margin: 0; padding: 0; }
  html, body { width: 1200px; height: 2400px; overflow: hidden; }
  body {
    background: var(--backdrop);
    font-family: "Source Sans 3", sans-serif;
    color: var(--ink);
    position: relative;
  }
  .card {
    position: absolute;
    left: 66px;
    width: 1065px;
    height: 590px;
    background: var(--card);
    box-shadow: 0 4px 12px rgba(0,0,0,0.25);
    overflow: hidden;
  }
  .card--front { top: 575px; }
  .card--back { top: 1235px; }

  .brand-name {
    font-family: "Source Sans 3", sans-serif;
    font-weight: 600;
    color: var(--ink);
    text-transform: uppercase;
    letter-spacing: 0.04em;
    line-height: 1;
    display: flex;
    align-items: center;
  }
  .brand-name__square {
    display: inline-block;
    background: var(--ink);
    flex: none;
  }
  .card--front .brand-name {
    position: absolute;
    left: 45px;
    top: 78px;
    font-size: 30px;
    gap: 18px;
  }
  .card--front .brand-name__square { width: 28px; height: 28px; }

  .holder {
    position: absolute;
    left: 607px;
    top: 58px;
  }
  .holder__name {
    font-size: 47px;
    font-weight: 700;
    line-height: 1.1;
  }
  .holder__name-last { color: var(--ink-soft); }
  .holder__title {
    font-size: 24px;
    font-weight: 600;
    margin-top: 2px;
  }

  .contact-list {
    position: absolute;
    left: 607px;
    top: 344px;
    list-style: none;
  }
  .contact-list__item {
    display: flex;
    align-items: center;
    height: 49px;
    font-size: 25px;
    font-weight: 400;
  }
  .contact-list__icon {
    width: 32px;
    height: 32px;
    border-radius: 4px;
    background: var(--ink);
    margin-right: 14px;
    flex: none;
  }

  .brand-decoration {
    position: absolute;
    left: 0;
    bottom: 0;
    width: 376px;
    height: 290px;
    background: linear-gradient(135deg, var(--deco-mid) 0%, var(--deco-light) 60%, #e6e6e6 100%);
  }

  .card--back .brand-name {
    position: absolute;
    left: 0;
    right: 0;
    top: 270px;
    justify-content: center;
    font-size: 50px;
    gap: 24px;
  }
  .card--back .brand-name__square { width: 44px; height: 44px; }

  .web-band {
    position: absolute;
    left: 0;
    right: 0;
    top: 505px;
    height: 56px;
    background: var(--band);
    color: var(--band-text);
    font-size: 32px;
    font-weight: 300;
    text-align: center;
    line-height: 56px;
    letter-spacing: 0.01em;
  }
</style>
</head>
<body>

<section class="card card--front">
  <div class="brand-name"><span class="brand-name__square"></span>Velmar Builds Ltd</div>

  <div class="holder">
    <h1 class="holder__name">Your <span class="holder__name-last">Namehere</span></h1>
    <p class="holder__title">Designation</p>
  </div>

  <ul class="contact-list">
    <li class="contact-list__item">
      <svg class="contact-list__icon" viewBox="0 0 32 32" aria-hidden="true">
        <rect width="32" height="32" rx="4" fill="#111"/>
        <path d="M10 7c1-.6 2-.3 2.5.6l1.6 3c.4.8.2 1.6-.5 2.1l-1.3 1c.9 2 2.5 3.6 4.5 4.6l1-1.3c.5-.7 1.4-.9 2.1-.5l3 1.6c.9.5 1.2 1.5.6 2.5l-.9 1.5c-.7 1.1-2 1.6-3.3 1.2C13.7 21.8 10.2 18.3 8.6 12.6c-.4-1.3.1-2.6 1.2-3.3z" fill="#fff"/>
      </svg>
      403-555-0148
    </li>
    <li class="contact-list__item">
      <svg class="contact-list__icon" viewBox="0 0 32 32" aria-hidden="true">
        <rect width="32" height="32" rx="4" fill="#111"/>
        <rect x="7" y="10" width="18" height="12" fill="#fff"/>
        <path d="M7 10l9 7 9-7M7 22l7-6M25 22l-7-6" stroke="#111" stroke-width="1.4" fill="none"/>
      </svg>
      projects@velmarbuilds-ex.com
    </li>
    <li class="contact-list__item">
      <svg class="contact-list__icon" viewBox="0 0 32 32" aria-hidden="true">
        <rect width="32" height="32" rx="4" fill="#111"/>
        <g stroke="#fff" stroke-width="1.4" fill="none">
          <circle cx="16" cy="16" r="8"/>
          <ellipse cx="16" cy="16" rx="3.5" ry="8"/>
          <path d="M8 16h16M9.2 12h13.6M9.2 20h13.6"/>
        </g>
      </svg>
      www.velmarbuilds-ex.com
    </li>
    <li class="contact-list__item">
      <svg class="contact-list__icon" viewBox="0 0 32 32" aria-hidden="true">
        <rect width="32" height="32" rx="4" fill="#111"/>
        <path d="M16 7a6 6 0 0 1 6 6c0 4.5-6 12-6 12s-6-7.5-6-12a6 6 0 0 1 6-6z" fill="#fff"/>
        <circle cx="16" cy="13" r="2.3" fill="#111"/>
      </svg>
      48 Sample St NE, Calgary, AB
    </li>
  </ul>

  <div class="brand-decoration" role="img" aria-label="Large brand mark decoration area in dark and light greys"></div>
</section>

<section class="card card--back">
  <div class="brand-name"><span class="brand-name__square"></span>Velmar Builds Ltd</div>
  <div class="web-band">www.velmarbuilds-ex.com</div>
</section>

</body>
</html>
```